Web Design Project for DJ

We need a web design for a DJ. Our client is a freelance DJ who already has a regular gig at a major night club but is looking to expand his exposure. He is located in a major metropolitan area and is looking for further gigs. He is hoping to generate further business via the website, including bookings via the site.

For reference his pagelinker page is here https://www.pagelinker.example/pages/DJ-Vorn/730162948415207

Following face to face discussions with the client today we have made a few small alterations to the brief.  We are hoping to have some images uploaded shortly.

Target Market(s)

Event planners, night club owners, radio stations, younger age groups (16-35)

Industry/Entity Type

Business

Requirements
Must have
• Name is DJVorn, this should obviously feature prominently. His current business card is attached as an example.

Links to Pagelinker and Tunedrift

Cool, modern look, slightly edgy.

Site will be built in Joomla, so a front page and secondary page template is required.
Nice to have
• Blog style layout to front page featuring recent and upcoming gigs.

Secondary pages may include a more expansive blog, a list of upcoming gigs, and a booking form.

Darker colour palettes preferred and use of same/similar fonts to those on the business card are an obvious plus

```html
<!DOCTYPE html>
<html lang="en">
<head>
<meta charset="utf-8">
<title>DJ-Vorn</title>
<link href="https://fonts.googleapis.com/css2?family=Oswald:wght@300;400;600;700&family=Open+Sans:wght@700&display=swap" rel="stylesheet">
<style>
:root{
  --page:#333333;
  --header-top:#0a0a0a;
  --header-bar:#1e1e1e;
  --footer:#000000;
  --nav-text:#c9c9c9;
  --heading-grey:#b0b0b0;
  --body-grey:#9a9a9a;
  --white:#ffffff;
  --green:#6fcf3a;
  --blue-top:#2fa4e8;
  --blue-bottom:#0a6fb8;
  --circle:#8a8a8a;
  --rule:#8c8c8c;
  --hero-teal:#3ec6e8;
  --hero-green:#7ef03a;
  --hero-pink:#d14be0;
}
*{box-sizing:border-box;margin:0;padding:0}
html,body{width:1200px;height:1185px;overflow:hidden;background:var(--page)}
body{position:relative;font-family:Arial,Helvetica,sans-serif}
a{text-decoration:none}
.abs{position:absolute}

/* header */
.site-header{left:0;top:0;width:1200px;height:76px;background:linear-gradient(var(--header-top) 0 48px,var(--header-bar) 48px 76px)}
.brand{left:40px;top:14px;display:flex;align-items:center;gap:12px;font-family:'Open Sans',sans-serif;font-weight:700;font-size:36px;color:var(--white);line-height:1}
.brand-dot{width:14px;height:14px;border-radius:50%;background:var(--white)}
.main-nav a{position:absolute;top:15px;font-family:'Oswald',sans-serif;font-weight:300;font-size:18px;color:var(--nav-text);text-transform:uppercase}

/* hero */
.hero{left:0;top:83px;width:1200px;height:470px;background:
  radial-gradient(ellipse 40% 35% at 50% 30%,#6a6f7a 0%,transparent 70%),
  linear-gradient(180deg,#1b3f9a 0%,#2a3fc4 30%,#6a2fc8 60%,#b43fd8 75%,#151515 88%,#0c0c0c 100%)}
.hero-line{font-family:'Oswald',sans-serif;font-weight:400;font-size:26px;line-height:33px;text-shadow:0 0 4px #000}
.hero-left{right:751px;top:104px;text-align:right}
.hero-right{left:676px;top:112px}
.t-green{color:var(--hero-green)}
.t-teal{color:var(--hero-teal)}
.t-pink{color:var(--hero-pink)}
.t-white{color:var(--white)}

/* band */
.band{left:0;top:553px;width:1200px;height:35px;background:linear-gradient(#2a2a2a,#4a4a4a 45%,#3a3a3a)}

/* booking button */
.booking-btn{left:26px;top:594px;width:312px;height:66px;border-radius:33px;background:#111;padding:6px}
.booking-btn span{display:flex;align-items:center;justify-content:center;width:100%;height:100%;border-radius:28px;background:linear-gradient(var(--blue-top),var(--blue-bottom));border:2px solid #5cc0f5;font-family:'Oswald',sans-serif;font-weight:300;font-size:30px;color:var(--white)}

.section-title{font-family:'Oswald',sans-serif;text-transform:uppercase;line-height:1}
.recent-title{left:36px;top:700px;font-weight:300;font-size:40px;color:var(--heading-grey)}
.upcoming-title{left:637px;top:610px;font-weight:600;font-size:36px;color:var(--heading-grey)}

.thumb{width:100px;height:84px}
.thumb-one{left:37px;top:757px;background:linear-gradient(135deg,#1c1a4a,#5a5ac8 55%,#1a2060)}
.thumb-two{left:37px;top:900px;background:linear-gradient(135deg,#1e5a1a,#6cd63a 45%,#1a2a1a)}
.gig-date{font-family:'Oswald',sans-serif;font-weight:600;font-size:22px;color:var(--heading-grey);line-height:22px}
.gig-text{font-size:14px;line-height:18px;color:var(--body-grey)}
.upcoming-text{font-size:14.5px;width:430px}
.more{font-size:11px;color:var(--white);text-transform:uppercase}
.recent-rule{left:39px;top:871px;width:463px;height:1px;background:var(--rule)}

.date-circle{width:74px;height:74px;border-radius:50%;background:var(--circle);display:flex;align-items:center;justify-content:center;font-family:'Oswald',sans-serif;font-weight:600;font-size:23px;color:var(--white)}

.contact{right:39px;text-align:right;font-family:'Oswald',sans-serif;font-weight:300;line-height:1;white-space:nowrap}
.phone{top:943px;font-size:40px;color:var(--white)}
.email{top:994px;font-size:36px;color:var(--green)}

/* footer */
.footer-rule{left:0;top:1050px;width:1200px;height:18px;background:linear-gradient(#555 0 4px,#2a2a2a 4px 8px,#777 8px 11px,#111 11px 18px)}
.site-footer{left:0;top:1068px;width:1200px;height:117px;background:var(--footer)}
.footer-nav{left:24px;top:1093px;font-size:13px;color:#dcdcdc;text-transform:uppercase}
.copyright{left:24px;top:1117px;font-size:12px;color:#777}
.social{top:1102px;display:flex;align-items:center;gap:7px;font-family:Arial,Helvetica,sans-serif;font-size:15px;color:var(--white)}
.social i{display:block;width:12px;height:12px;background:var(--white)}
</style>
</head>
<body>

<header class="abs site-header">
  <div class="abs brand"><span class="brand-dot"></span>DJ-Vorn</div>
  <nav class="main-nav">
    <a style="left:514px" href="#">Home</a>
    <a style="left:606px" href="#">Booking</a>
    <a style="left:720px" href="#">Recent Gigz</a>
    <a style="left:856px" href="#">Upcoming Gigz</a>
    <a style="left:1014px" href="#">Gallery</a>
    <a style="left:1124px" href="#">Contact</a>
  </nav>
</header>

<section class="abs hero" role="img" aria-label="DJ at his decks in front of glowing equalizer bars and stage lights"></section>
<p class="abs hero-line hero-left"><span class="t-green">Catch DJ Vorn</span> <span class="t-teal">at</span><br><span class="t-teal">Brightwater's Tannery</span><br><span class="t-pink">on Kessel.</span></p>
<p class="abs hero-line hero-right"><span class="t-pink">Every</span> <span class="t-teal">Thursday</span> <span class="t-white">for</span> <span class="t-green">"Circuit Kids"</span><br><span class="t-pink">Saturday</span> <span class="t-white">for</span> <span class="t-green">"Afterglow Saturdays"</span><span class="t-pink">.</span></p>

<div class="abs band"></div>

<a class="abs booking-btn" href="#"><span>REQUEST FOR BOOKING</span></a>

<h2 class="abs section-title recent-title">Recent Gigz</h2>

<div class="abs thumb thumb-one" role="img" aria-label="Photo from a recent gig"></div>
<div class="abs gig-date" style="left:160px;top:756px">06.11.2013</div>
<p class="abs gig-text" style="left:162px;top:779px;width:350px">New mix up and running, ready for auditory pleasure making - just in time for your Australia Day festivities! Enjoy the beginning of a new trilogy ....</p>
<a class="abs more" style="left:163px;top:839px" href="#">More</a>
<div class="abs recent-rule"></div>

<div class="abs thumb thumb-two" role="img" aria-label="Photo from a recent gig"></div>
<div class="abs gig-date" style="left:160px;top:898px">05.28.2013</div>
<p class="abs gig-text" style="left:162px;top:922px;width:350px">New mix up and running, ready for auditory pleasure making - just in time for your Australia Day festivities! Enjoy the beginning of a new trilogy of ....</p>
<a class="abs more" style="left:161px;top:980px" href="#">More</a>

<h2 class="abs section-title upcoming-title">Upcoming Gigz</h2>

<div class="abs date-circle" style="left:638px;top:666px">07.11</div>
<p class="abs gig-text upcoming-text" style="left:736px;top:668px">New mix up and running, ready for auditory pleasure making - just in time for your Australia Day festivities! Enjoy the beginning of a new trilogy of mini-mixes I'll be releasing over the next few weeks. As always, love your feedback ....</p>
<a class="abs more" style="left:736px;top:747px" href="#">More</a>

<div class="abs date-circle" style="left:638px;top:799px">06.25</div>
<p class="abs gig-text upcoming-text" style="left:736px;top:803px">New mix up and running, ready for auditory pleasure making - just in time for your Australia Day festivities! Enjoy the beginning of a new trilogy of mini-mixes I'll be releasing over the next few weeks. As always, love your feedback. ...</p>
<a class="abs more" style="left:736px;top:889px" href="#">More</a>

<p class="abs contact phone">phone :&nbsp; 0491 570 156</p>
<p class="abs contact email">vornH.Q@mail.example</p>

<div class="abs footer-rule"></div>
<footer class="abs site-footer"></footer>
<p class="abs footer-nav">Home | Booking | Recent Gigz | Upcoming Gigz | Gallery | Contact</p>
<p class="abs copyright">© Copyright DJ-Vorn. All Rights Reserved 2013.</p>
<a class="abs social" style="left:905px" href="https://www.pagelinker.example/pages/DJ-Vorn/730162948415207"><i></i>Pagelinker</a>
<a class="abs social" style="left:1010px" href="#"><i></i>Tunedrift</a>
<a class="abs social" style="left:1105px" href="#"><i></i>Chirpline</a>

</body>
</html>
```